Mobile Oil Change company needs a flyer to promote new business

We need a flyer to 1) print & handout and 2) email out to potential customers. We are a mobile oil change company that comes to our customer locations to perform the work instead of customers going to traditional oil change companies. We have a 21 point inspection with our oil change. (21 point inspection details will not be on the flyer). Would like to keep the flyer simple but creative. I'm attaching 1) the write-up we created, 2) our logo (logo color is dark teal on white but other combinations are included if you wanted to propose a different color combination), and 3) additional services we offer. Logo font is Alegreya Sans.
Would like the additional services listed with icons and brief descriptions (similar to attachment) without pricing. Company website for reference is www.brookmerelubeworks.com.

Target Market(s)

Companies with many service vehicles such as Oil & Gas service companies, heating and air conditioning companies, utility companies, police departments, etc. Companies that prioritize convenience and maintenance first.

Font styles to use
Sans Serif

Colors
00a990

Requirements
Must have
• Simple but creative design with our logo at top of the flyer. Additional Services (details in document supplied) can be smaller and less prominent than other "main" content listed in the CONTENT document supplied.
Should not have
• Do not use animated character graphics in the flyer and limit (1) stock photos to A small area in the flyer.

```html
<!DOCTYPE html>
<html lang="en">
<head>
<meta charset="utf-8">
<title>Brookmere Lube Works – Mobile Oil Change Flyer</title>
<link href="https://fonts.googleapis.com/css2?family=Alegreya+Sans:wght@400;500;700;800&family=Oswald:wght@500;600&display=swap" rel="stylesheet">
<style>
:root{
  --deep-teal:#174f52;
  --brand-teal:#00a990;
  --white:#ffffff;
  --ink:#123f42;
  --drop-warm:#d9a24a;
  --drop-cool:#8e9aa0;
}
*{margin:0;padding:0;box-sizing:border-box}
html,body{width:902px;height:1200px;overflow:hidden;background:#e6e6e6}
body{font-family:"Alegreya Sans",sans-serif;color:var(--white)}
.flyer{position:relative;width:902px;height:1200px;overflow:hidden;background:var(--white)}
.backdrop{position:absolute;inset:0}
.brand{position:absolute;left:56px;top:44px;width:380px;text-align:center;font-family:"Alegreya Sans",sans-serif;font-weight:800;color:var(--white);line-height:1}
.brand .name{font-size:58px;letter-spacing:2px;display:block}
.brand .tag{font-size:25px;letter-spacing:4px;display:block;margin-top:6px}
.headline{position:absolute;left:52px;top:268px;color:var(--deep-teal)}
.headline .lead{font-family:"Oswald",sans-serif;font-weight:600;font-size:68px;line-height:1;letter-spacing:1px;display:block}
.headline .accent{font-family:"Alegreya Sans",sans-serif;font-weight:700;font-size:50px;line-height:1;color:var(--brand-teal);display:block;margin-top:12px}
.headline .close{font-family:"Alegreya Sans",sans-serif;font-weight:700;font-size:41px;line-height:1;display:block;margin-top:14px}
.photo-drop{position:absolute;left:510px;top:24px;width:392px;height:536px}
.intro{position:absolute;left:54px;top:484px;width:440px;font-size:22px;line-height:30px;font-weight:400}
.steps{position:absolute;left:34px;top:0;list-style:none}
.step{position:absolute;left:0;width:470px;display:flex;align-items:center;gap:16px;font-size:21px;line-height:27px;font-weight:500}
.step .icon{flex:none;width:60px;height:60px;border-radius:50%;background:var(--white);border:3px solid var(--brand-teal);display:flex;align-items:center;justify-content:center}
.step .icon svg{width:32px;height:32px}
.highlights{position:absolute;left:544px;top:600px;width:330px;list-style:none}
.highlights li{position:relative;padding-left:38px;font-size:15px;font-weight:700;line-height:19px;margin-bottom:14px}
.highlights li::before{content:"";position:absolute;left:2px;top:4px;width:13px;height:13px;border-radius:50%;background:var(--deep-teal)}
.extras{position:absolute;left:533px;top:706px;width:333px;height:398px;border:2px solid var(--white);border-radius:26px}
.extras-title{position:absolute;left:50%;top:-16px;transform:translateX(-50%);background:var(--white);color:var(--ink);font-weight:800;font-size:19px;padding:2px 14px;border-radius:14px;white-space:nowrap}
.extra{position:absolute;left:10px;display:flex;align-items:center;gap:12px;font-size:17px;font-weight:700}
.extra .icon{flex:none;width:48px;height:48px;border-radius:50%;background:var(--white);border:2px solid var(--deep-teal);display:flex;align-items:center;justify-content:center}
.extra .icon svg{width:28px;height:28px}
.phone-pill{position:absolute;left:30px;top:1036px;width:432px;height:62px;background:var(--white);border-radius:31px;display:flex;align-items:center;padding-left:20px;gap:18px;color:var(--deep-teal);box-shadow:0 3px 6px rgba(0,0,0,.25)}
.phone-pill svg{width:42px;height:42px}
.phone-pill .number{font-weight:800;font-size:40px;letter-spacing:.5px}
.or-badge{position:absolute;left:62px;top:1094px;width:28px;height:28px;border-radius:50%;background:var(--white);color:var(--ink);font-size:14px;font-weight:700;display:flex;align-items:center;justify-content:center}
.email{position:absolute;left:62px;top:1122px;display:flex;align-items:center;gap:14px;font-size:22px;font-weight:700}
.email svg{width:28px;height:22px}
.website{position:absolute;left:558px;top:1133px;display:flex;align-items:center;gap:14px;font-size:22px;font-weight:700}
.website svg{width:22px;height:22px}
</style>
</head>
<body>
<main class="flyer">
  <svg class="backdrop" width="902" height="1200" viewBox="0 0 902 1200" aria-hidden="true">
    <rect width="902" height="1200" fill="#ffffff"/>
    <path d="M0 0H902V150Q640 175 0 210Z" fill="#174f52"/>
    <path d="M0 222Q320 200 640 160" fill="none" stroke="#00a990" stroke-width="7"/>
    <path d="M0 452H902V1200H0Z" fill="#00a990"/>
    <path d="M440 452H902V540Q700 590 560 480Q520 452 440 452Z" fill="#ffffff"/>
    <path d="M0 458H420Q450 458 468 472L505 500Q522 516 522 540V955Q522 1010 470 1010H0Z" fill="#174f52"/>
    <path d="M0 458H420Q450 458 468 472L505 500" fill="none" stroke="#00a990" stroke-width="6"/>
    <path d="M440 1200Q470 1120 560 1118H902V1200Z" fill="#174f52"/>
  </svg>

  <header class="brand">
    <span class="name">BROOKMERE</span>
    <span class="tag">LUBE WORKS</span>
  </header>

  <svg class="photo-drop" viewBox="0 0 392 536" role="img" aria-label="Photo of motor oil being poured through an orange funnel into an engine">
    <defs>
      <linearGradient id="dropFill" x1="0" y1="0" x2="1" y2="1">
        <stop offset="0" stop-color="#e9e4dc"/>
        <stop offset=".5" stop-color="#d9a24a"/>
        <stop offset="1" stop-color="#5d676c"/>
      </linearGradient>
    </defs>
    <path d="M192 4C250 100 392 190 392 340A196 196 0 0 1 0 340C0 190 134 100 192 4Z" fill="#ffffff"/>
    <path d="M192 26C246 115 374 200 374 340A182 182 0 0 1 10 340C10 200 138 115 192 26Z" fill="url(#dropFill)"/>
  </svg>

  <h1 class="headline">
    <span class="lead">HASSLE FREE</span>
    <span class="accent">OIL CHANGES</span>
    <span class="close">ON YOUR TERMS</span>
  </h1>

  <p class="intro">Our simple 5-step process lets you schedule an appointment and get service to save time and money:</p>

  <ol class="steps">
    <li class="step" style="top:588px">
      <span class="icon"><svg viewBox="0 0 32 32"><path d="M8 4l5 5-3 3q3 6 9 9l3-3 5 5-4 4Q10 26 4 8Z" fill="#123f42"/></svg></span>
      Call or email us to schedule service
    </li>
    <li class="step" style="top:670px">
      <span class="icon"><svg viewBox="0 0 32 32"><path d="M22 4a6 6 0 0 0-6 8L5 23l4 4 11-11a6 6 0 0 0 8-6l-4 3-3-1-1-3Z" fill="#123f42"/></svg></span>
      Our highly trained technicians come to you for service
    </li>
    <li class="step" style="top:752px">
      <span class="icon"><svg viewBox="0 0 32 32"><path d="M6 18l3-8h14l3 8v7h-4v-3H10v3H6Z" fill="#123f42"/><circle cx="10" cy="19" r="2" fill="#fff"/><circle cx="22" cy="19" r="2" fill="#fff"/></svg></span>
      Service is performed quickly on your vehicle
    </li>
    <li class="step" style="top:832px">
      <span class="icon"><svg viewBox="0 0 32 32"><rect x="4" y="8" width="24" height="17" rx="2" fill="#123f42"/><path d="M5 9l11 9 11-9" fill="none" stroke="#fff" stroke-width="2"/></svg></span>
      Pay agreed-upon pricing and receipt is emailed to you
    </li>
    <li class="step" style="top:924px">
      <span class="icon"><svg viewBox="0 0 32 32"><path d="M16 4a8 8 0 0 0-8 8v7l-3 4h22l-3-4v-7a8 8 0 0 0-8-8Z" fill="#123f42"/><circle cx="16" cy="26" r="3" fill="#123f42"/></svg></span>
      Services performed are tracked electronically and reminders created
    </li>
  </ol>

  <ul class="highlights">
    <li>High quality synthetic oil used is best suited for commercial vehicles</li>
    <li>Service includes a 21-point inspection</li>
  </ul>

  <section class="extras">
    <h2 class="extras-title">ADDITIONAL SERVICES</h2>
    <div class="extra" style="top:28px"><span class="icon"><svg viewBox="0 0 28 28"><rect x="5" y="5" width="18" height="18" rx="2" fill="none" stroke="#123f42" stroke-width="2"/><path d="M10 6v16M14 6v16M18 6v16" stroke="#123f42" stroke-width="2"/></svg></span>Engine Air Filter Replacement</div>
    <div class="extra" style="top:86px"><span class="icon"><svg viewBox="0 0 28 28"><rect x="6" y="4" width="16" height="20" rx="2" fill="none" stroke="#123f42" stroke-width="2"/><path d="M8 10q3-3 6 0t6 0M8 15q3-3 6 0t6 0" fill="none" stroke="#123f42" stroke-width="2"/></svg></span>Cabin Air Filter Replacement</div>
    <div class="extra" style="top:144px"><span class="icon"><svg viewBox="0 0 28 28"><path d="M3 10Q14 2 25 10L14 25Z" fill="none" stroke="#123f42" stroke-width="2"/><path d="M14 25L8 10" stroke="#123f42" stroke-width="2"/></svg></span>Wiperblade Replacement</div>
    <div class="extra" style="top:206px"><span class="icon"><svg viewBox="0 0 28 28"><circle cx="14" cy="14" r="10" fill="none" stroke="#123f42" stroke-width="2.5"/><circle cx="14" cy="14" r="3" fill="#123f42"/><path d="M4 13h7M17 13h7M14 17v7" stroke="#123f42" stroke-width="2.5"/></svg></span>Power Steering Fluid Flush</div>
    <div class="extra" style="top:266px"><span class="icon"><svg viewBox="0 0 28 28"><rect x="6" y="4" width="11" height="20" rx="1" fill="none" stroke="#123f42" stroke-width="2"/><rect x="8" y="7" width="7" height="5" fill="#123f42"/><path d="M17 10h3v10a2 2 0 0 0 3 0V8l-3-3" fill="none" stroke="#123f42" stroke-width="2"/></svg></span>Fuel System Treatment</div>
    <div class="extra" style="top:326px"><span class="icon"><svg viewBox="0 0 28 28"><circle cx="14" cy="14" r="10" fill="none" stroke="#123f42" stroke-width="2"/><circle cx="14" cy="14" r="4" fill="none" stroke="#123f42" stroke-width="2"/><path d="M5 8a12 12 0 0 1 6-5" fill="none" stroke="#123f42" stroke-width="2"/></svg></span>Brake Fluid Flush</div>
  </section>

  <div class="phone-pill">
    <svg viewBox="0 0 42 42" aria-hidden="true"><path d="M9 4l7 7-4 4q4 9 13 13l4-4 7 7-5 6Q11 35 4 10Z" fill="#111"/><path d="M26 8a9 9 0 0 1 8 8M26 3a14 14 0 0 1 13 13" fill="none" stroke="#111" stroke-width="2.5"/></svg>
    <span class="number">(833) 555-0142</span>
  </div>
  <span class="or-badge">or</span>
  <div class="email">
    <svg viewBox="0 0 28 22" aria-hidden="true"><rect x="1" y="2" width="26" height="18" rx="2" fill="#123f42"/><path d="M2 3l12 9 12-9" fill="none" stroke="#fff" stroke-width="2"/></svg>
    Sales@BrookmereLubeWorks.com
  </div>
  <div class="website">
    <svg viewBox="0 0 22 22" aria-hidden="true"><circle cx="11" cy="11" r="9" fill="none" stroke="#fff" stroke-width="2"/><ellipse cx="11" cy="11" rx="4" ry="9" fill="none" stroke="#fff" stroke-width="1.5"/><path d="M2 11h18" stroke="#fff" stroke-width="1.5"/></svg>
    www.BrookmereLubeWorks.com
  </div>
</main>
</body>
</html>
```